Complete Printing Package
Business Cards, Stationary, Envelopes, Presentation Folder
We love all the designs, but no one has submitted a minimalist design as mentioned in the brief. Very subtle color, only very light lines with thin stroke.
Anyone up for it?
We would just like something a little different to consider.
Notes:
1. We will not publish cell phone numbers on anything except business cards.
2. We will not publish email addresses on anything except business cards.
3. We like the look of "www.q-t-x.net" stretched out to "w w w . q - t - x . n e t"
4. On the green "H" element in the logo, there are some edge lines that define the H that we would like deleted when used as a watermark or shadow.
5. Can we see some concepts with the green shown as #8BA50B ?
Note to all:
We are looking for designs with straight lines throughout.
#78 & #79, can you change the black portions of your designs to gray?
Note to all, there seems to be many designs using black prominently throughout the design. We prefer the use of gray. We feel that the use of black is too harsh. If the designs look a little off with the black portion of the graphic in the logo, we are open to changing the black in the logo to gray as well.
Note to all, can you also include a fax cover page?
Note to all, I prefer a white background for the letterhead, envelopes and business cards.
For the proposal folder, we will consider grey, perhaps black and white backgrounds as well.
thanks!
Uploaded the template our printer uses for presentation folders. Please use this in preparing the presentation.
Thanks to all!

```html
<!DOCTYPE html>
<html lang="en">
<head>
<meta charset="utf-8">
<title>Quarrytonex stationery set</title>
<link href="https://fonts.googleapis.com/css2?family=Montserrat:wght@400;700;800&display=swap" rel="stylesheet">
<style>
:root{
  --bg:#3a3a3a;
  --paper:#ffffff;
  --green:#8ba50b;
  --green-dark:#7a920a;
  --gray:#5e5e5e;
  --faint:#f0f0f0;
  --ink:#2b2b2b;
}
*{margin:0;padding:0;box-sizing:border-box}
html,body{width:1200px;height:238px;overflow:hidden}
body{background:radial-gradient(ellipse at 40% 30%,#474747,var(--bg) 70%);font-family:"Montserrat",sans-serif;position:relative}
.piece{position:absolute;background:var(--paper);box-shadow:0 1px 3px rgba(0,0,0,.45);overflow:hidden}
.brand{display:flex;flex-direction:column;align-items:center;line-height:1}
.brand .mark{background:var(--green)}
.brand .name{font-weight:800;color:var(--gray);letter-spacing:.02em;white-space:nowrap}
.brand .tag{color:var(--gray);letter-spacing:.18em;white-space:nowrap}
.mini .mark{width:5px;height:5px;margin-bottom:1px}
.mini .name{font-size:4px}
.mini .tag{font-size:2px;margin-top:1px}
.hero-brand{position:absolute;left:10px;top:8px}
.hero-brand .mark{width:16px;height:16px;margin-bottom:4px}
.hero-brand .name{font-size:12px;color:#fff}
.hero-brand .tag{font-size:4px;color:#cfcfcf;margin-top:2px}
.small{font-size:2.6px;color:var(--gray);line-height:1.4;white-space:nowrap}
.web{position:absolute;left:0;right:0;font-size:2.6px;color:var(--gray);text-align:center;white-space:nowrap}
.rule{position:absolute;height:1px;background:var(--green)}
.watermark{position:absolute;background:var(--faint)}
</style>
</head>
<body>

<div class="brand hero-brand">
  <span class="mark"></span>
  <span class="name">QUARRYTONEX</span>
  <span class="tag">DEVELOPMENT GROUP</span>
</div>

<!-- business cards -->
<div class="piece" style="left:8px;top:66px;width:50px;height:29px">
  <div class="brand mini" style="position:absolute;left:0;right:0;top:9px"><span class="mark"></span><span class="name">QUARRYTONEX</span><span class="tag">DEVELOPMENT GROUP</span></div>
</div>
<div class="piece" style="left:62px;top:66px;width:50px;height:29px">
  <div class="small" style="position:absolute;left:4px;top:5px"><b>Jordan Vale</b><br>Managing Director<br>T 555 014 2338</div>
  <div class="web" style="bottom:4px">w w w . q - t - x . n e t</div>
  <div class="rule" style="left:0;right:0;bottom:0;height:2px"></div>
</div>
<div class="piece" style="left:8px;top:99px;width:50px;height:29px">
  <div class="brand mini" style="position:absolute;left:0;right:0;top:6px"><span class="mark"></span><span class="name">QUARRYTONEX</span></div>
  <div class="rule" style="left:0;right:0;bottom:0;height:7px"></div>
</div>
<div class="piece" style="left:62px;top:99px;width:50px;height:29px">
  <div class="watermark" style="left:16px;top:5px;width:18px;height:18px"></div>
  <div class="rule" style="left:0;right:0;bottom:0;height:2px"></div>
</div>

<!-- letterhead -->
<div class="piece" style="left:125px;top:8px;width:72px;height:102px">
  <div class="brand mini" style="position:absolute;left:0;right:0;top:5px"><span class="mark"></span><span class="name">QUARRYTONEX</span><span class="tag">DEVELOPMENT GROUP</span></div>
  <div class="watermark" style="left:20px;top:36px;width:32px;height:32px"></div>
  <div class="rule" style="left:8px;right:8px;bottom:8px"></div>
  <div class="web" style="bottom:3px">w w w . q - t - x . n e t</div>
</div>

<!-- fax cover -->
<div class="piece" style="left:308px;top:8px;width:72px;height:102px">
  <div class="brand mini" style="position:absolute;left:0;right:0;top:5px"><span class="mark"></span><span class="name">QUARRYTONEX</span><span class="tag">DEVELOPMENT GROUP</span></div>
  <div class="watermark" style="left:20px;top:36px;width:32px;height:32px"></div>
  <div class="rule" style="left:8px;right:8px;bottom:8px"></div>
  <div class="web" style="bottom:3px">w w w . q - t - x . n e t</div>
</div>

<!-- compliment slips -->
<div class="piece" style="left:535px;top:28px;width:90px;height:38px">
  <div class="brand mini" style="position:absolute;left:5px;top:5px"><span class="mark"></span><span class="name">QUARRYTONEX</span></div>
  <div class="rule" style="left:5px;right:5px;bottom:6px"></div>
</div>
<div class="piece" style="left:535px;top:72px;width:90px;height:38px">
  <div class="brand mini" style="position:absolute;left:5px;top:5px"><span class="mark"></span><span class="name">QUARRYTONEX</span></div>
  <div class="rule" style="left:0;right:0;bottom:0;height:3px"></div>
</div>

<!-- envelopes -->
<div class="piece" style="left:642px;top:12px;width:92px;height:44px">
  <svg width="92" height="44" style="position:absolute;left:0;top:0"><polygon points="0,0 92,0 46,24" fill="var(--ink)"/></svg>
  <div class="brand mini" style="position:absolute;left:0;right:0;top:4px"><span class="mark"></span><span class="name" style="color:#fff">QUARRYTONEX</span></div>
</div>
<div class="piece" style="left:642px;top:62px;width:92px;height:48px">
  <svg width="92" height="48" style="position:absolute;left:0;top:0"><polyline points="0,0 46,20 92,0" fill="none" stroke="var(--green)" stroke-width="1"/></svg>
  <div class="rule" style="left:0;right:0;bottom:0;height:3px"></div>
</div>

<!-- presentation folder -->
<div class="piece" style="left:748px;top:8px;width:214px;height:102px">
  <div class="brand" style="position:absolute;left:0;right:0;top:30px"><span class="mark" style="width:10px;height:10px;margin-bottom:3px"></span><span class="name" style="font-size:8px">QUARRYTONEX</span><span class="tag" style="font-size:3px;margin-top:2px">DEVELOPMENT GROUP</span></div>
  <div style="position:absolute;left:0;right:0;bottom:0;height:12px;background:var(--green)"></div>
</div>
<div class="piece" style="left:966px;top:8px;width:222px;height:102px;background:var(--green)">
  <div class="watermark" style="left:78px;top:22px;width:50px;height:50px;background:rgba(255,255,255,.12)"></div>
  <svg width="222" height="102" style="position:absolute;left:0;top:0"><polygon points="0,66 222,56 222,102 0,102" fill="var(--green-dark)" opacity=".6"/></svg>
</div>

</body>
</html>
```